Sorlen cards

I want a simple business card that pops.
Logo on one side.
On side two i want.
"Are you thinking about a new building on your property, or renovating an existing structure? Contact".....
Owners Name: Dale Whitcombe
Owners Phone number: 717-555-0192
Address:4716 Oxtail Ridge RD, Bedford, PA 15522
Committed to Quality, Service, and Integrity

```html
<!DOCTYPE html>
<html lang="en">
<head>
<meta charset="utf-8">
<title>Sorlen Builders LLC – Business Card</title>
<link rel="stylesheet" href="https://fonts.googleapis.com/css2?family=Lato:wght@400;700;900&display=swap">
<style>
  :root {
    --backdrop: #3b3b3c;
    --card: #ffffff;
    --brown-dark: #43301f;
    --brown-mid: #5a4330;
    --ink: #3d3026;
    --rule: #5a4330;
  }
  * { margin: 0; padding: 0; box-sizing: border-box; }
  html, body { width: 1200px; height: 689px; overflow: hidden; }
  body {
    background: var(--backdrop);
    font-family: "Lato", Arial, sans-serif;
    display: flex;
    align-items: center;
    justify-content: center;
    gap: 50px;
  }
  .card {
    width: 530px;
    height: 303px;
    background: var(--card);
    border-radius: 22px;
    position: relative;
    box-shadow: 0 14px 30px rgba(0,0,0,0.35);
    overflow: hidden;
  }
  /* Front */
  .card--front {
    display: flex;
    align-items: center;
    justify-content: center;
    gap: 18px;
  }
  .brand-mark {
    width: 46px;
    height: 46px;
    background: var(--brown-dark);
    flex-shrink: 0;
  }
  .brand-name {
    color: var(--brown-dark);
    font-weight: 900;
    text-transform: uppercase;
    line-height: 1;
  }
  .brand-name .primary { display: block; font-size: 64px; letter-spacing: 1px; }
  .brand-name .secondary { display: block; font-size: 25px; letter-spacing: 4px; margin-top: 6px; text-align: center; }

  /* Back */
  .card--back { display: flex; align-items: center; }
  .back-brand {
    width: 190px;
    flex-shrink: 0;
    display: flex;
    flex-direction: column;
    align-items: center;
    gap: 10px;
  }
  .back-brand .brand-mark { width: 34px; height: 34px; }
  .back-brand .brand-name { font-size: 26px; letter-spacing: 1px; }
  .divider {
    width: 1px;
    height: 220px;
    background: var(--rule);
    flex-shrink: 0;
  }
  .contact {
    padding-left: 26px;
    padding-right: 18px;
    color: var(--ink);
  }
  .tagline {
    font-size: 11.5px;
    font-weight: 900;
    color: var(--brown-mid);
    text-transform: uppercase;
    letter-spacing: 0.6px;
    line-height: 1.35;
    width: 270px;
    margin-bottom: 12px;
  }
  .owner-name {
    font-size: 26px;
    font-weight: 900;
    text-transform: uppercase;
    color: var(--brown-dark);
    line-height: 1.05;
  }
  .owner-role { font-size: 14px; margin-bottom: 10px; }
  .company { font-size: 12.5px; font-weight: 900; text-transform: uppercase; color: var(--brown-mid); }
  .address { font-size: 13.5px; margin-bottom: 6px; }
  .phone {
    font-size: 18px;
    font-weight: 900;
    color: var(--brown-dark);
    display: flex;
    align-items: center;
    gap: 6px;
  }
  .phone svg { width: 15px; height: 15px; }
  .motto {
    margin-top: 8px;
    font-size: 11px;
    font-weight: 700;
    letter-spacing: 0.4px;
    color: var(--brown-mid);
  }
</style>
</head>
<body>
  <section class="card card--front" aria-label="Card front">
    <span class="brand-mark" aria-hidden="true"></span>
    <h1 class="brand-name">
      <span class="primary">Sorlen</span>
      <span class="secondary">Builders LLC</span>
    </h1>
  </section>

  <section class="card card--back" aria-label="Card back">
    <div class="back-brand">
      <span class="brand-mark" aria-hidden="true"></span>
      <span class="brand-name">Sorlen</span>
    </div>
    <div class="divider" aria-hidden="true"></div>
    <div class="contact">
      <p class="tagline">Are you thinking about a new building on your property, or renovating an existing structure? Contact.....</p>
      <h2 class="owner-name">Dale Whitcombe</h2>
      <p class="owner-role">Owner</p>
      <p class="company">Sorlen Builders LLC</p>
      <p class="address">4716 Oxtail Ridge RD, Bedford, PA 15522</p>
      <p class="phone">
        <svg viewBox="0 0 24 24" aria-hidden="true"><path fill="#43301f" d="M6.6 10.8a15.1 15.1 0 0 0 6.6 6.6l2.2-2.2a1 1 0 0 1 1-.25 11.4 11.4 0 0 0 3.6.57 1 1 0 0 1 1 1V20a1 1 0 0 1-1 1A17 17 0 0 1 3 4a1 1 0 0 1 1-1h3.5a1 1 0 0 1 1 1c0 1.25.2 2.45.57 3.57a1 1 0 0 1-.25 1z"/></svg>
        717-555-0192
      </p>
      <p class="motto">Committed to Quality, Service, and Integrity</p>
    </div>
  </section>
</body>
</html>
```